Orthopedic Landing Page Website Design

We are working with a Orthopedic Medical Group in California. They provide orthopedic services throughout California.

Some sites to use for inspiration:
https://www.kvreth.com
https://belvantrix.com
https://www.quellbridgevex.com
https://tarnwickfelvaspring.com

Thank you for taking the time to consider designing a website for us. We are web developers based in Stockton, CA, USA. Most of our projects go through the same process. Understanding this process may help you win a project with us. We custom-code all of our websites in-house. We don’t have any requirements as to what tools you use for your design, but we ask that you follow these guidelines.

IMAGES:
If you use any images or icons in the design, we ask that you have a link to the asset so we can purchase the image/icon. Most of the designs we submit do not have the customer’s images on them unless they have some great images. Be creative; show us the feeling you are trying to portray with your image choices. Use any royalty-free site you choose. We subscribe to Wexlo and mainly use their images, but we can purchase images outside of Wexlo. PLEASE NOTE: we will not submit designs to clients with watermarks on the images.

FONTS:
We ask that you identify the fonts you’re using in the design. This can be done in a message if you want. We typically use Pelmira Fonts and Wexlo Fonts.

CONTENT:
We're always open to different content and ideas. We often submit designs with stock images so the client can see our vision. We typically take pictures after the website launch to use their images with our vision. Lorem Ipsum is fine for paragraphs, but we ask that you make the Headers with correct English. We want to be able to show the vision and identify the sections of the website.

INSPIRATION:
We typically add a couple of links in the brief of websites we like to help you get started in your design.

REVISIONS:
We do not often ask for revisions of the designs unless we see something in the design that may not appeal to the client. If there are slight changes that we want to make, we do that in the development process.

FEEDBACK:
We rarely give feedback on designs during the design process. We are working on many website projects and do not have the time to provide feedback. We usually respond if your request is well thought out and asks specific questions, but a note asking “feedback, please” usually goes unanswered.

```html
<!DOCTYPE html>
<html lang="en">
<head>
<meta charset="utf-8">
<title>Orva Ridgeline Orthopedic</title>
<link href="https://fonts.googleapis.com/css2?family=Raleway:wght@500;600;700;800&family=Roboto:wght@400;500;700&display=swap" rel="stylesheet">
<style>
:root{
  --red:#d41f3b;
  --blue:#2b57a7;
  --blue-deep:#1f4692;
  --ink:#2a2a2a;
  --text:#6b6b6b;
  --dark:#1b1b1d;
  --light:#f7f7f7;
  --white:#ffffff;
}
*{box-sizing:border-box;margin:0;padding:0}
html,body{width:1200px;height:3908px;overflow:hidden}
body{position:relative;font-family:'Roboto',sans-serif;color:var(--ink);background:var(--white)}
.abs{position:absolute}
.btn{position:absolute;display:flex;align-items:center;justify-content:center;gap:8px;border-radius:30px;color:var(--white);font:700 15px 'Roboto',sans-serif;text-transform:uppercase}
.btn-red{background:var(--red)}
.btn-blue{background:var(--blue)}
.btn .arrow{width:15px;height:15px}

/* header */
.site-header{position:absolute;left:0;top:0;width:1200px;height:110px;background:var(--light)}
.brand{left:111px;top:18px}
.brand-name{font:500 58px 'Raleway',sans-serif;color:var(--blue);letter-spacing:12px;line-height:1}
.brand-sub{font:500 13px 'Roboto',sans-serif;color:var(--ink);letter-spacing:2px;text-transform:uppercase;margin-top:4px}
.call{left:626px;top:18px;display:flex;gap:12px;align-items:center}
.call-icon{width:36px;height:36px;border-radius:50%;background:var(--blue);display:flex;align-items:center;justify-content:center}
.call small{display:block;font-size:12px;color:#888}
.call strong{font-size:18px;color:var(--ink)}
.nav{left:488px;top:80px;display:flex;gap:24px;font-size:15px;color:var(--ink)}
.nav span.sep{color:#555}

/* hero */
.hero{left:0;top:110px;width:1200px;height:685px;background:linear-gradient(160deg,#7b6a5f 0%,#4a3b33 40%,#8d8c8a 75%,#c9c9c7 100%)}
.hero-text{left:0;top:195px;width:1200px;text-align:center;color:var(--white)}
.hero-text .pre{font:700 32px 'Raleway',sans-serif;letter-spacing:-0.5px}
.hero-text h1{font:800 68px/1.08 'Raleway',sans-serif;margin-top:14px;text-transform:uppercase}

/* about */
.about-photo{left:103px;top:808px;width:457px;height:457px;border-radius:50%;background:radial-gradient(circle at 55% 55%,#e9a36c 0%,#c99a84 35%,#6f6d75 70%,#4d4c55 100%);box-shadow:0 10px 20px rgba(0,0,0,.25)}
.about-ring{left:98px;top:803px}
.about-copy{left:625px;top:848px;width:462px}
h2{font:600 34px 'Raleway',sans-serif;color:var(--ink)}
.lead{font-size:14px;line-height:26.5px;color:var(--text)}
.about-copy .lead{margin-top:14px}
.about-copy .lead + .lead{margin-top:8px}

/* services */
.section-title{left:0;width:1200px;text-align:center}
.service{position:absolute;width:290px;height:323px}
.service span{position:absolute;left:0;right:0;bottom:30px;text-align:center;color:var(--white);font:700 17px 'Roboto',sans-serif;text-shadow:0 1px 3px rgba(0,0,0,.5)}

/* patients */
.patients-photo{left:542px;top:1902px;width:546px;height:375px;background:linear-gradient(120deg,#cdd7cf 0%,#d9a88a 45%,#f2f2f4 70%,#c9d3dd 100%)}
.patients-card{left:111px;top:1931px;width:503px;height:319px;background:var(--white);box-shadow:0 6px 24px rgba(0,0,0,.15);padding:28px 46px}
.patients-card .lead{font-size:14px;line-height:25.5px;margin-top:12px}

/* blog */
.blog-card{position:absolute;width:309px;height:453px;background:var(--white);box-shadow:0 6px 18px rgba(0,0,0,.18);border-radius:4px;text-align:center}
.blog-card .thumb{margin:8px;height:228px;border-radius:3px}
.blog-card h3{font:700 17px 'Roboto',sans-serif;margin-top:24px;color:var(--ink)}
.blog-card p{font-size:14px;line-height:23px;color:var(--text);margin:14px 20px 0}
.blog-card .btn{left:83px;bottom:30px;width:141px;height:43px}

/* contact */
.contact{left:0;top:3004px;width:1200px;height:560px;background:linear-gradient(180deg,#2a59ad,#2a53a0)}
.field{position:absolute;background:var(--white);border:2px solid #d7d7d7;border-radius:26px;font-size:13px;color:#999;padding:0 28px;display:flex;align-items:center}

/* footer */
.footer{left:0;top:3420px;width:1200px;height:488px;background:var(--dark)}
.foot-col{position:absolute;top:3588px;color:var(--white)}
.foot-col h4{font:700 18px 'Roboto',sans-serif;margin-bottom:18px}
.foot-col ul{list-style:none;font-size:14px}
.foot-col li{line-height:31px}
.contact-list li{display:flex;gap:18px;align-items:flex-start;line-height:24px;margin-bottom:12px}
.social{width:32px;height:32px;border-radius:50%;border:2px solid var(--white);display:inline-block;margin-right:8px}
</style>
</head>
<body>

<header class="site-header">
  <div class="abs brand">
    <div class="brand-name">ORVA</div>
    <div class="brand-sub">Ridgeline Orthopedic</div>
  </div>
  <div class="abs call">
    <div class="call-icon"><svg width="18" height="18" viewBox="0 0 24 24"><path fill="#fff" d="M6.6 10.8a15 15 0 0 0 6.6 6.6l2.2-2.2a1 1 0 0 1 1-.25 11.4 11.4 0 0 0 3.6.57 1 1 0 0 1 1 1V20a1 1 0 0 1-1 1A17 17 0 0 1 3 4a1 1 0 0 1 1-1h3.5a1 1 0 0 1 1 1c0 1.25.2 2.45.57 3.57a1 1 0 0 1-.25 1z"/></svg></div>
    <div><small>Call Us Today</small><strong>+1 888 888 8888</strong></div>
  </div>
  <div class="btn btn-red" style="left:844px;top:17px;width:244px;height:44px;font-size:15px">Request an Appointment</div>
  <nav class="abs nav">
    <span>HOME</span><span class="sep">|</span><span>ABOUT US</span><span class="sep">|</span><span>SERVICES</span><span class="sep">|</span><span>TEAM</span><span class="sep">|</span><span>BLOG</span><span class="sep">|</span><span>CONTACT US</span>
  </nav>
</header>

<section>
  <div class="abs hero" role="img" aria-label="Runner holding a sore knee on an outdoor road"></div>
  <svg class="abs" style="left:0;top:680px" width="1200" height="120" viewBox="0 0 1200 120">
    <path d="M0 115 Q600 -20 1200 115 L1200 120 L0 120 Z" fill="var(--red)"/>
    <path d="M0 120 Q600 -5 1200 120 Z" fill="#fff"/>
  </svg>
  <div class="abs hero-text">
    <div class="pre">WELCOME TO</div>
    <h1>Orva Ridgeline<br>Orthopedic</h1>
  </div>
  <div class="btn btn-red" style="left:497px;top:540px;width:206px;height:47px;font-size:17px">Get Started
    <svg class="arrow" viewBox="0 0 16 16"><circle cx="8" cy="8" r="8" fill="#fff"/><path d="M6.5 4.5 10 8l-3.5 3.5" stroke="var(--red)" stroke-width="2" fill="none"/></svg></div>
</section>

<section>
  <div class="abs about-photo" role="img" aria-label="Hands holding a knee with the joint highlighted"></div>
  <svg class="abs about-ring" width="467" height="467" viewBox="0 0 467 467">
    <path d="M233.5 3 A230.5 230.5 0 0 1 233.5 464" stroke="var(--red)" stroke-width="4" fill="none"/>
    <path d="M233.5 464 A230.5 230.5 0 0 1 233.5 3" stroke="var(--blue)" stroke-width="4" fill="none"/>
  </svg>
  <div class="abs about-copy">
    <h2>About Us</h2>
    <p class="lead">Lorem ipsum dolor sit amet, consectetur adipiscing elit, sed do eiusmod tempor incididunt ut labore et dolore magna aliqua. Ut enim ad minim veniam, quis nostrud exercitation ullamco laboris nisi ut aliquip ex ea commodo consequat. Duis aute irure dolor in reprehenderit .</p>
    <p class="lead">Nostrud exercitation ullamco laboris nisi ut aliquip ex ea commodo consequat. Duis aute irure dolor in reprehenderit in voluptate velit esse cillum dolore eu fugiat nulla pariatur. Excepteur sint occaecat cupidatat non proident sunt in culpa qui officia deserunt mollit anim consectetur adipiscing elit sed do eiusmod tempor incididunt labore dolored.</p>
  </div>
  <div class="btn btn-red" style="left:625px;top:1172px;width:184px;height:46px">Learn More
    <svg class="arrow" viewBox="0 0 16 16"><circle cx="8" cy="8" r="8" fill="#fff"/><path d="M6.5 4.5 10 8l-3.5 3.5" stroke="var(--red)" stroke-width="2" fill="none"/></svg></div>
</section>

<section>
  <h2 class="abs section-title" style="top:1335px">Our Services</h2>
  <div class="service" style="left:0;top:1417px;background:linear-gradient(135deg,#5d7fb0,#3b63a8 50%,#9aa8b6)" role="img" aria-label="Surgeons performing an orthopedic operation"><span>Orthopedic Surgery</span></div>
  <div class="service" style="left:303px;top:1452px;background:linear-gradient(135deg,#e6e4e2,#e6a88a 50%,#8fa9d6)" role="img" aria-label="Gloved hands examining a foot"><span>impact advisory</span></div>
  <div class="service" style="left:607px;top:1417px;background:linear-gradient(135deg,#8a6b57,#e9ecef 55%,#cfd6dc)" role="img" aria-label="Injection being given in the shoulder"><span>Injections</span></div>
  <div class="service" style="left:910px;top:1452px;background:linear-gradient(135deg,#e8e6e3,#a1745c 50%,#d06a2a 70%,#8a8580)" role="img" aria-label="Man holding his lower back with spine highlighted"><span>Patient Resources</span></div>
</section>

<section>
  <div class="abs patients-photo" role="img" aria-label="Doctor examining a patient's knee"></div>
  <div class="abs patients-card">
    <h2>We Put Patients First</h2>
    <p class="lead">Lorem ipsum dolor sit amet, consectetur adipiscing elit, sed do eiusmod tempor incididunt ut labore et dolore magna aliqua. Ut enim ad minim veniam, quis nostrud exercitation ullamco laboris nisi ut aliquip ex ea commodo consequat. Duis aute irure dolor in reprehenderit in voluptate velit esse cillum dolore eu fugiat nulla pariatur. Excepteur sint occaecat cupidatat non proident.</p>
  </div>
  <div class="btn btn-red" style="left:158px;top:2172px;width:185px;height:43px">Learn More
    <svg class="arrow" viewBox="0 0 16 16"><circle cx="8" cy="8" r="8" fill="#fff"/><path d="M6.5 4.5 10 8l-3.5 3.5" stroke="var(--red)" stroke-width="2" fill="none"/></svg></div>
</section>

<section>
  <h2 class="abs section-title" style="top:2357px">Our Blog</h2>
  <article class="blog-card" style="left:111px;top:2461px">
    <div class="thumb" style="background:linear-gradient(135deg,#3d3b3c,#a9674a 50%,#c9c9c9)" role="img" aria-label="Runner holding an injured knee"></div>
    <h3>Lorem ipsum dolor sit amet</h3>
    <p>Lorem ipsum dolor sit amet consectetur adipiscing eiusmod tempor incididunt ut labore et dolore magna aliquat enim.</p>
    <div class="btn btn-blue">Read More</div>
  </article>
  <article class="blog-card" style="left:445px;top:2436px">
    <div class="thumb" style="background:linear-gradient(135deg,#eceff2,#c7ced6 50%,#6e8fb3)" role="img" aria-label="Physiotherapist treating a seated patient's leg"></div>
    <h3>Lorem ipsum dolor sit amet</h3>
    <p>Diabetes is the leading cause of new blindness in the 20-64 year old age group. Type 2 diabetes develops when...</p>
    <div class="btn btn-blue">Read More</div>
  </article>
  <article class="blog-card" style="left:779px;top:2461px">
    <div class="thumb" style="background:linear-gradient(135deg,#dfe5ea,#9bb0c8 45%,#3e63a8)" role="img" aria-label="Patient in a leg brace walking with crutches"></div>
    <h3>Lorem ipsum dolor sit amet</h3>
    <p>Diabetes is the leading cause of new blindness in the 20-64 year old age group. Type 2 diabetes develops when...</p>
    <div class="btn btn-blue">Read More</div>
  </article>
</section>

<footer class="abs footer"></footer>
<section>
  <div class="abs contact" role="img" aria-label="Faint blue-tinted photo of a clinic"></div>
  <svg class="abs" style="left:0;top:3420px" width="1200" height="150" viewBox="0 0 1200 150">
    <path d="M0 10 Q600 220 1200 10 L1200 0 L0 0 Z" fill="#2a53a0"/>
    <path d="M0 10 Q600 220 1200 10 L1200 40 Q600 160 0 40 Z" fill="#fff" opacity="0"/>
    <path d="M0 10 Q600 200 1200 10" stroke="#fff" stroke-width="6" fill="none"/>
  </svg>
  <h2 class="abs section-title" style="top:3040px;color:var(--white)">Contact Us</h2>
  <div class="field" style="left:193px;top:3127px;width:395px;height:53px">Name</div>
  <div class="field" style="left:193px;top:3192px;width:395px;height:53px">Email Address</div>
  <div class="field" style="left:193px;top:3258px;width:395px;height:53px">Phone Number</div>
  <div class="field" style="left:609px;top:3127px;width:398px;height:188px;border-radius:20px;align-items:flex-start;padding-top:20px">Message</div>
  <div class="btn btn-red" style="left:499px;top:3353px;width:207px;height:52px;font-size:17px">Submit Now
    <svg class="arrow" viewBox="0 0 16 16"><circle cx="8" cy="8" r="8" fill="#fff"/><path d="M6.5 4.5 10 8l-3.5 3.5" stroke="var(--red)" stroke-width="2" fill="none"/></svg></div>
</section>

<div class="foot-col" style="left:111px">
  <h4>Contact Us</h4>
  <ul class="contact-list">
    <li><svg width="12" height="16" viewBox="0 0 12 16"><path d="M6 0a6 6 0 0 1 6 6c0 4-6 10-6 10S0 10 0 6a6 6 0 0 1 6-6z" fill="var(--red)"/><circle cx="6" cy="6" r="2" fill="var(--dark)"/></svg><span>123,Lorem ipsum dolor sit<br>consectetur adipiscing.</span></li>
    <li><svg width="14" height="12" viewBox="0 0 14 12"><rect width="14" height="12" rx="1" fill="var(--red)"/><path d="M0 1l7 5 7-5" stroke="var(--dark)" stroke-width="1.4" fill="none"/></svg><span>info@orva-ortho.com</span></li>
    <li><svg width="14" height="14" viewBox="0 0 24 24"><path fill="var(--red)" d="M6.6 10.8a15 15 0 0 0 6.6 6.6l2.2-2.2a1 1 0 0 1 1-.25 11.4 11.4 0 0 0 3.6.57 1 1 0 0 1 1 1V20a1 1 0 0 1-1 1A17 17 0 0 1 3 4a1 1 0 0 1 1-1h3.5a1 1 0 0 1 1 1c0 1.25.2 2.45.57 3.57a1 1 0 0 1-.25 1z"/></svg><span>+1 888 888 8888</span></li>
    <li><svg width="14" height="14" viewBox="0 0 14 14"><rect y="3" width="14" height="11" rx="1" fill="var(--red)"/><rect x="3" width="8" height="4" fill="var(--red)"/></svg><span>123 456 7890</span></li>
  </ul>
</div>
<div class="foot-col" style="left:369px">
  <h4>Quick Links</h4>
  <ul><li>Home</li><li>About Us</li><li>Services</li><li>Team</li><li>Blog</li><li>Contact Us</li></ul>
</div>
<div class="foot-col" style="left:551px">
  <h4>Other Links</h4>
  <ul style="margin-top:-4px"><li>Terms &amp; Condition</li><li>Privacy Policy</li><li>Updates</li><li>Support</li><li>Contact</li></ul>
</div>
<div class="foot-col" style="left:711px">
  <h4>Subscribe for Updates</h4>
  <div style="position:relative;width:377px;height:46px">
    <div style="position:absolute;left:3px;top:0;width:238px;height:46px;background:#fff;border-radius:23px;font-size:12px;color:#888;display:flex;align-items:center;padding-left:22px">Email Address</div>
    <div class="btn btn-red" style="left:245px;top:0;width:132px;height:46px;font-size:17px">Submit</div>
  </div>
  <div style="margin-top:20px;font-size:13px;font-weight:500;display:flex;gap:8px;align-items:center">
    <svg width="12" height="12" viewBox="0 0 12 12"><rect x="1" y="1" width="10" height="10" rx="2" stroke="#fff" fill="none"/><path d="M3 6l2 2 4-5" stroke="#fff" stroke-width="1.5" fill="none"/></svg>Yes, Please Contact me.</div>
  <div style="margin-top:18px"><span class="social"></span><span class="social"></span><span class="social"></span></div>
</div>

<div class="abs" style="left:111px;top:3832px;width:978px;height:1px;background:#3a3a3c"></div>
<div class="abs" style="left:0;top:3853px;width:1200px;text-align:center;color:#fff;font-size:13px">© 2023&nbsp; Orva&nbsp; |&nbsp; All Rights Reserved&nbsp; |</div>

</body>
</html>
```